Website for Brisbeck Current Glide

Require a website for a river float in the City of Edmonton. Located on North Saskatchewan River. Will need to be a coded website with incorporated booking system through Fare Harbor software.

Pages include
Home
Pricing
About
FAQ
Contact

Brisbeck Current Glide is an activity based business that will have customers floating down the North Saskatchewan river in Edmonton AB. The site will have all information needed and a full reservation system. The project was launched to provide people in the Edmonton area a favorite summer activity.

Here are similar websites to reference what our business will be doing and what we are looking for.

mellowbendcanoehire.example
pinegulchloopers.example

Target Market(s)

Families, Groups, Individuals, Anyone who wants to explore the river

Industry/Entity Type

Activities based business/ Outdoor recreational/ River Float

Coding

Coded - Design and coding required

Number of Pages Required

5+ page

Colors
0054AA
0677BA
7BADD7
CADEEF
E8F1F8
F0912C
F2A743
F7CA91
FBE8D2
FDF5EE

```html
<!DOCTYPE html>
<html lang="en">
<head>
<meta charset="utf-8">
<title>Brisbeck Current Glide</title>
<link href="https://fonts.googleapis.com/css2?family=Poppins:wght@400;500;600;700&display=swap" rel="stylesheet">
<style>
:root{
  --navy:#0b2d5e;
  --navy-deep:#08244d;
  --sky:#4ec3e6;
  --sky-pale:#d4eef8;
  --orange:#ff5f17;
  --white:#ffffff;
  --ink:#1d2535;
  --grey:#8a93a3;
  --line:#b9c0cc;
}
*{margin:0;padding:0;box-sizing:border-box}
html,body{width:1200px;height:3438px;overflow:hidden;background:var(--white)}
body{font-family:"Poppins",sans-serif;color:var(--ink);position:relative}
.abs{position:absolute}

/* top bar */
.topbar{left:0;top:0;width:1200px;height:47px;background:var(--sky);color:var(--white);font-size:14px;font-weight:500;z-index:5}
.topbar .address{left:92px;top:13px;display:flex;align-items:center;gap:8px}
.topbar .follow{right:80px;top:13px;display:flex;align-items:center;gap:12px}
.dot{width:14px;height:14px;border:2px solid var(--white);border-radius:50%;display:inline-block}

/* nav */
.navbar{left:0;top:47px;width:1200px;height:87px;background:var(--white);border-bottom:1px solid #e3e7ee;z-index:3}
.brand-badge{left:88px;top:47px;width:176px;height:140px;background:var(--white);border-radius:0 0 88px 88px;display:flex;flex-direction:column;align-items:center;justify-content:center;z-index:4}
.brand-badge .mark{width:34px;height:34px;border-radius:50%;background:var(--sky);margin-bottom:6px}
.brand-badge .name{font-weight:700;font-size:15px;color:var(--navy);text-align:center;line-height:1.15}
.menu{left:451px;top:34px;display:flex;gap:43px;font-size:15px;font-weight:500;color:var(--ink)}
.menu .active{color:var(--navy);font-weight:600}
.pill{display:flex;align-items:center;justify-content:space-between;border-radius:30px;font-weight:600;font-size:16px;padding:0 6px 0 28px}
.pill .knob{width:40px;height:40px;border-radius:50%;background:var(--white);display:flex;align-items:center;justify-content:center}
.pill .knob i{width:24px;height:24px;border-radius:50%;background:var(--sky);display:block}
.talk{left:942px;top:20px;width:165px;height:48px;background:var(--navy);color:var(--white)}

/* hero */
.hero{left:0;top:134px;width:1200px;height:604px;background:linear-gradient(180deg,#2e5786 0%,#244a78 55%,#1b3a62 100%);overflow:hidden}
.hero-title{left:92px;top:175px;color:var(--white)}
.hero-title h1{font-size:60px;font-weight:700;line-height:1;letter-spacing:1px}
.hero-title h2{font-size:36px;font-weight:500;letter-spacing:9px;margin-top:12px;line-height:1.2}
.hero-title p{font-size:19px;font-weight:500;line-height:1.5;margin-top:16px;letter-spacing:.5px}
.book-light{left:92px;top:525px;width:185px;height:50px;background:var(--sky);color:var(--navy);z-index:2}
.hero-art{left:605px;top:72px;width:520px;height:520px;border-radius:50%;background:linear-gradient(160deg,#7fd3ee 0%,#4ab6dc 50%,#2e8fbf 100%);border:6px solid rgba(255,255,255,.18)}
.bubbles circle{fill:none;stroke:var(--sky);stroke-width:3}

/* section heads */
.kicker-rings circle{fill:none;stroke-width:2.6}
.head-navy{color:var(--navy);font-weight:700}
.head-sky{color:var(--sky);font-weight:600}

/* included */
.included-head{left:0;top:832px;width:1200px;text-align:center}
.included-head .l1{font-size:43px;line-height:54px}
.included-head .l2{font-size:43px;line-height:54px}
.included-head p{font-size:17px;margin-top:10px;color:var(--ink)}
.gear{top:1033px;width:230px;text-align:center}
.gear .ring{position:relative;width:230px;height:265px}
.gear .arc{position:absolute;left:0;top:0;width:230px;height:230px}
.gear .photo{position:absolute;left:10px;top:44px;width:220px;height:220px;border-radius:50%}
.gear .label{font-size:16px;font-weight:600;margin-top:30px;line-height:1.6}
.learn{left:502px;top:1412px;width:198px;height:50px;background:var(--navy);color:var(--white)}

/* floating */
.floating{left:0;top:1555px;width:1200px;height:550px;overflow:hidden;background:var(--navy)}
.floating .photo{left:0;top:0;width:800px;height:550px;background:linear-gradient(135deg,#3f6b4a 0%,#557f5a 35%,#b8323a 65%,#4d7c60 100%)}
.floating .panel{left:0;top:0}
.floating .copy{left:737px;top:92px;width:370px;color:var(--white)}
.floating h3{font-size:40px;line-height:48px}
.floating h3 .l1{color:var(--white);font-weight:700}
.floating h3 .l2{color:var(--sky);font-weight:600}
.floating p{font-size:17px;line-height:29px;margin-top:20px}
.book-dark{left:738px;top:1992px;width:185px;height:50px;background:var(--sky);color:var(--navy)}

/* contact */
.contact-badge{left:93px;top:2233px;width:412px;height:412px}
.contact-badge .inner{position:absolute;left:32px;top:32px;width:348px;height:348px;border-radius:50%;background:var(--sky-pale);display:flex;flex-direction:column;align-items:center;justify-content:center}
.contact-badge .mark{width:110px;height:110px;border-radius:50%;background:var(--sky);margin-bottom:18px}
.contact-badge .name{font-weight:700;font-size:30px;color:var(--navy);text-align:center;line-height:1.15}
.contact-head{left:590px;top:2222px}
.contact-head h3{font-size:43px;line-height:56px}
.contact-head p{font-size:17px;margin-top:10px}
.field{border:1.5px solid var(--line);border-radius:3px;font-size:16px;color:var(--grey);padding:0 17px;display:flex;align-items:center;background:var(--white)}
.field.area{align-items:flex-start;padding-top:13px}
.send{left:590px;top:2627px;width:188px;height:50px;background:var(--navy);color:var(--white)}

/* footer */
.footer-wave{left:0;top:2770px;width:1200px;height:330px}
.footer-body{left:0;top:3000px;width:1200px;height:438px;background:var(--navy)}
.follow-us{right:93px;top:2905px;display:flex;align-items:center;gap:14px;color:var(--white);font-weight:600;font-size:20px}
.follow-us .box{width:45px;height:45px;border:1.5px solid rgba(255,255,255,.6);display:flex;align-items:center;justify-content:center}
.follow-us .box i{width:14px;height:14px;border:2px solid var(--white);border-radius:50%}
.foot-h{font-size:20px;font-weight:600;color:var(--white)}
.connect{left:92px;top:3058px;color:var(--white)}
.contact-row{display:flex;gap:21px;margin-top:20px;font-size:17px;line-height:28px}
.contact-row .ic{width:45px;height:45px;border-radius:3px;display:flex;align-items:center;justify-content:center;flex:none;background:#1d5aa3}
.subscribe{left:92px;top:3267px;width:325px;height:50px;border-radius:25px;background:var(--white);overflow:hidden}
.subscribe span{position:absolute;left:32px;top:14px;font-size:15px;color:var(--grey)}
.subscribe .go{position:absolute;right:0;top:0;width:60px;height:50px;background:var(--orange);display:flex;align-items:center;justify-content:center}
.navigation{left:563px;top:3058px;color:var(--white)}
.navigation ul{list-style:none;margin-top:16px;font-size:17px;line-height:40px}
.daily{left:840px;top:3058px;width:268px;text-align:center;color:var(--white)}
.daily .mark{width:150px;height:150px;border-radius:50%;background:var(--sky);margin:36px auto 12px}
.daily .name{font-weight:700;font-size:24px;color:var(--white);line-height:1.15}
.copyright{left:0;top:3376px;width:1200px;text-align:center;font-size:14px;color:#8fa3c2}
</style>
</head>
<body>

<!-- top bar -->
<div class="abs topbar">
  <div class="abs address">
    <svg width="14" height="18" viewBox="0 0 14 18"><path d="M7 0C3.1 0 0 3.1 0 7c0 5 7 11 7 11s7-6 7-11c0-3.9-3.1-7-7-7z" fill="#fff"/><circle cx="7" cy="7" r="2.6" fill="#4ec3e6"/></svg>
    Address : Willowbank Landing 4120 62 Ave NW, Edmonton, AB
  </div>
  <div class="abs follow">Follow Us: <span class="dot"></span><span class="dot"></span><span class="dot"></span></div>
</div>

<!-- navigation -->
<header class="abs navbar">
  <nav class="abs menu">
    <span class="active">HOME</span><span>PRICING</span><span>ABOUT</span><span>FAQ</span><span>CONTACT</span>
  </nav>
  <div class="abs pill talk">Let’s Talk
    <span class="knob"><svg width="22" height="22" viewBox="0 0 24 24"><path d="M6.6 10.8a15 15 0 006.6 6.6l2.2-2.2c.3-.3.7-.4 1-.2 1.1.4 2.3.6 3.6.6.6 0 1 .4 1 1V20c0 .6-.4 1-1 1A17 17 0 013 4c0-.6.4-1 1-1h3.5c.6 0 1 .4 1 1 0 1.3.2 2.5.6 3.6.1.3 0 .7-.2 1z" fill="none" stroke="#0b2d5e" stroke-width="1.8"/></svg></span>
  </div>
</header>
<div class="abs brand-badge"><span class="mark"></span><span class="name">Brisbeck<br>Current Glide</span></div>

<!-- hero -->
<section class="abs hero" role="img" aria-label="Dusk view of the river valley and downtown skyline">
  <div class="abs hero-title">
    <h1>BRISBECK</h1>
    <h2>CURRENT GLIDE</h2>
    <p>Float the North Saskatchewan through<br>downtown Edmonton</p>
  </div>
  <div class="abs hero-art" role="img" aria-label="Illustration of an arch bridge over the river with a float raft"></div>
  <svg class="abs bubbles" style="left:588px;top:470px" width="60" height="70"><circle cx="12" cy="14" r="8"/><circle cx="42" cy="38" r="14"/><circle cx="20" cy="54" r="6"/></svg>
</section>
<svg class="abs kicker-rings" style="left:125px;top:296px" width="30" height="30"><circle cx="10" cy="8" r="6" stroke="#fff"/><circle cx="22" cy="22" r="5" stroke="#4ec3e6"/></svg>
<svg class="abs kicker-rings" style="left:478px;top:296px" width="30" height="34"><circle cx="10" cy="8" r="5" stroke="#4ec3e6"/><circle cx="22" cy="22" r="6" stroke="#fff"/></svg>
<div class="abs pill book-light">Book Now<span class="knob"><i></i></span></div>

<!-- included -->
<svg class="abs kicker-rings" style="left:406px;top:805px" width="32" height="32"><circle cx="10" cy="10" r="7" stroke="#0b2d5e"/><circle cx="24" cy="24" r="5" stroke="#4ec3e6"/></svg>
<div class="abs included-head">
  <div class="l1 head-navy">SHUTTLE SERVICE</div>
  <div class="l2 head-sky">AND GEAR INCLUDED</div>
  <p>We provide everything you need including</p>
</div>
<svg class="abs kicker-rings" style="left:822px;top:890px" width="32" height="36"><circle cx="10" cy="10" r="7" stroke="#0b2d5e"/><circle cx="22" cy="26" r="5" stroke="#4ec3e6"/></svg>

<div class="abs gear" style="left:92px">
  <div class="ring">
    <svg class="arc" viewBox="0 0 230 230"><path d="M5 140A115 115 0 0 1 185 10 120 120 0 0 0 5 140z" fill="#0b2d5e"/></svg>
    <div class="photo" role="img" aria-label="Yellow shuttle bus parked by the riverside" style="background:linear-gradient(160deg,#c9dbe8 0%,#e5b23a 55%,#8a8f96 100%)"></div>
  </div>
  <div class="label">ROUND TRIP<br>SHUTTLE SERVICE</div>
</div>
<div class="abs gear" style="left:357px">
  <div class="ring">
    <svg class="arc" viewBox="0 0 230 230"><path d="M5 140A115 115 0 0 1 185 10 120 120 0 0 0 5 140z" fill="#4ec3e6"/></svg>
    <div class="photo" role="img" aria-label="Close-up of red and yellow float tubes" style="background:linear-gradient(135deg,#e52b2b 0%,#d61f2a 50%,#f1e07a 100%)"></div>
  </div>
  <div class="label">FLOAT TUBE</div>
</div>
<div class="abs gear" style="left:620px">
  <div class="ring">
    <svg class="arc" viewBox="0 0 230 230"><path d="M5 140A115 115 0 0 1 185 10 120 120 0 0 0 5 140z" fill="#ff5f17"/></svg>
    <div class="photo" role="img" aria-label="Child wearing an orange lifejacket" style="background:linear-gradient(180deg,#3e6a68 0%,#b8896a 45%,#ef7a1a 100%)"></div>
  </div>
  <div class="label">LIFEJACKET</div>
</div>
<div class="abs gear" style="left:884px">
  <div class="ring">
    <svg class="arc" viewBox="0 0 230 230"><path d="M5 140A115 115 0 0 1 185 10 120 120 0 0 0 5 140z" fill="#0b2d5e"/></svg>
    <div class="photo" role="img" aria-label="Yellow paddle blade resting on calm water" style="background:radial-gradient(circle at 55% 45%,#c99a2a 0%,#6a6a5a 40%,#3c4146 100%)"></div>
  </div>
  <div class="label">PADDLE &amp; MORE</div>
</div>
<div class="abs pill learn">Learn More<span class="knob"><i></i></span></div>

<!-- floating -->
<section class="abs floating">
  <div class="abs photo" role="img" aria-label="Group in red helmets and lifejackets paddling a raft"></div>
  <svg class="abs panel" width="1200" height="550" viewBox="0 0 1200 550">
    <path d="M760 0C640 60 610 210 640 330 670 450 730 520 760 550H1200V0Z" fill="#ff5f17"/>
    <path d="M780 0C670 70 640 210 665 330 690 440 740 510 800 550H1200V0Z" fill="#0b2d5e"/>
  </svg>
  <svg class="abs kicker-rings" style="left:740px;top:62px" width="32" height="32"><circle cx="10" cy="10" r="7" stroke="#fff"/><circle cx="24" cy="24" r="5" stroke="#4ec3e6"/></svg>
  <div class="abs copy">
    <h3><span class="l1">FLOATING 7 &amp;</span><br><span class="l2">DAYS A WEEK</span></h3>
    <p>Our priority is to make sure everyone has a safe and fun time on the river. Safety demonstrations are provided and staff are available to assist in any way. Whether you are a family with children, larger group or just want a relaxing way to explore the river, this is a must try activity.</p>
  </div>
  <svg class="abs kicker-rings" style="left:1018px;top:142px" width="30" height="34"><circle cx="10" cy="10" r="6" stroke="#fff"/><circle cx="20" cy="24" r="5" stroke="#4ec3e6"/></svg>
</section>
<div class="abs pill book-dark">Book Now<span class="knob"><i></i></span></div>

<!-- contact -->
<div class="abs contact-badge">
  <svg class="abs" style="left:0;top:0" width="412" height="412" viewBox="0 0 412 412">
    <path d="M4 206A202 202 0 0 1 408 206" fill="none" stroke="#0b2d5e" stroke-width="3" stroke-dasharray="3 6" stroke-linecap="round"/>
    <path d="M4 212A202 202 0 0 0 408 212" fill="none" stroke="#4ec3e6" stroke-width="5"/>
  </svg>
  <div class="inner"><span class="mark"></span><span class="name">Brisbeck<br>Current Glide</span></div>
</div>
<svg class="abs kicker-rings" style="left:610px;top:2200px" width="34" height="30"><circle cx="10" cy="10" r="7" stroke="#0b2d5e"/><circle cx="26" cy="22" r="5" stroke="#4ec3e6"/></svg>
<div class="abs contact-head">
  <h3><span class="head-navy">CONTACT</span> <span class="head-sky">US</span></h3>
  <p>We’d love to hear from you!</p>
</div>
<svg class="abs kicker-rings" style="left:872px;top:2238px" width="30" height="34"><circle cx="10" cy="10" r="6" stroke="#0b2d5e"/><circle cx="20" cy="24" r="5" stroke="#4ec3e6"/></svg>
<div class="abs field" style="left:590px;top:2354px;width:252px;height:50px">Name</div>
<div class="abs field" style="left:855px;top:2354px;width:252px;height:50px">Email Address</div>
<div class="abs field" style="left:590px;top:2418px;width:252px;height:50px">Phone</div>
<div class="abs field" style="left:855px;top:2418px;width:252px;height:50px">Service</div>
<div class="abs field area" style="left:590px;top:2481px;width:517px;height:118px">Leave your mesage !</div>
<div class="abs pill send">Send Now<span class="knob"><i></i></span></div>

<!-- footer -->
<div class="abs footer-body"></div>
<svg class="abs footer-wave" viewBox="0 0 1200 330" preserveAspectRatio="none">
  <path d="M0 120C120 220 300 240 520 150 760 50 1020 -20 1200 90V330H0Z" fill="#ff5f17"/>
  <path d="M0 230C140 290 320 300 520 230 760 140 1000 80 1200 150V330H0Z" fill="#fff"/>
  <path d="M0 240C140 300 320 310 520 240 760 150 1000 95 1200 170V330H0Z" fill="#0b2d5e"/>
</svg>
<div class="abs follow-us">FOLLOW US:
  <span class="box"><i></i></span><span class="box"><i></i></span><span class="box"><i></i></span>
</div>

<div class="abs connect">
  <div class="foot-h">CONNECT</div>
  <div class="contact-row">
    <span class="ic"><svg width="14" height="18" viewBox="0 0 14 18"><path d="M7 0C3.1 0 0 3.1 0 7c0 5 7 11 7 11s7-6 7-11c0-3.9-3.1-7-7-7z" fill="#fff"/><circle cx="7" cy="7" r="2.6" fill="#1d5aa3"/></svg></span>
    <span>Willowbank Landing<br>4120 62 Ave NW, Edmonton, AB</span>
  </div>
  <div class="contact-row">
    <span class="ic"><svg width="18" height="14" viewBox="0 0 18 14"><rect x="1" y="1" width="16" height="12" rx="2" fill="#fff"/><path d="M1 3l8 5 8-5" fill="none" stroke="#1d5aa3" stroke-width="1.5"/></svg></span>
    <span>Email:<br>info@brisbeckcurrentglide.example</span>
  </div>
</div>
<div class="abs subscribe"><span>Email Address..</span>
  <div class="go"><svg width="18" height="18" viewBox="0 0 18 18"><path d="M3 2l13 7-13 7 3-7z" fill="#fff"/></svg></div>
</div>

<div class="abs navigation">
  <div class="foot-h">NAVIGATION</div>
  <ul><li>Home</li><li>Pricing</li><li>About</li><li>FAQ</li><li>Contact</li></ul>
</div>

<div class="abs daily">
  <div class="foot-h">FLOATING 7 DAYS A WEEK</div>
  <div class="mark"></div>
  <div class="name">Brisbeck<br>Current Glide</div>
</div>

<div class="abs copyright">Copyright © 2022 Brisbeck Current Glide. All rights reserved.</div>

</body>
</html>
```